Beacon Law Stationary - Law Firm

I am looking for a designer who can help me design letterhead and envelopes consistent with our new business cards. Feel free to reach out to me directly at ned@beaconlawgroup.example. Thank you!! Visit beaconlawgroup.example to see our site and the attached files for creative assets.

Target Market(s)

Anyone needing a lawyer

Font styles to use
Other font styles liked:
• Adobe Caslon Pro

Requirements
Must have
• Adobe Caslon Pro font
Full color
Nice to have
• My photo on front along with 2/3 face of camo - see mock up for example of what I have in mind.

American colors - similar to the ones found on my website and gold.

```html
<!DOCTYPE html>
<html lang="en">
<head>
<meta charset="utf-8">
<title>Beacon Law Stationery</title>
<link rel="stylesheet" href="https://fonts.googleapis.com/css2?family=Libre+Caslon+Text:wght@400;700&family=Montserrat:wght@300;400;700&family=Lato:wght@300;400&family=Encode+Sans+Condensed:wght@300&display=swap">
<style>
  :root {
    --backdrop: #d9e4ef;
    --paper: #ffffff;
    --navy: #0d2647;
    --navy-soft: #163462;
    --gold: #b5a365;
    --ink: #5b5b5b;
    --ink-dark: #4d4d4d;
  }
  * { margin: 0; padding: 0; box-sizing: border-box; }
  html, body { width: 1200px; height: 831px; overflow: hidden; }
  body { background: var(--backdrop); position: relative; font-family: "Lato", sans-serif; }

  .sheet { position: absolute; background: var(--paper); overflow: hidden; }
  .footer-band {
    position: absolute; left: 0; right: 0; bottom: 0;
    background: linear-gradient(180deg, var(--navy-soft), var(--navy));
  }
  .brand-name {
    position: absolute; font-family: "Libre Caslon Text", serif; font-weight: 700;
    color: var(--gold); letter-spacing: 0.06em; white-space: nowrap; text-transform: uppercase;
  }

  /* Letterhead */
  .letterhead { left: 117px; top: 111px; width: 430px; height: 609px; }
  .letterhead .footer-band { height: 96px; }
  .letterhead .brand-name { right: 40px; top: 92px; font-size: 17px; }
  .letter-date { position: absolute; left: 41px; top: 185px; font-family: "Montserrat", sans-serif; font-weight: 300; font-size: 9.5px; color: var(--ink); }
  .recipient-name { position: absolute; left: 40px; top: 201px; font-family: "Montserrat", sans-serif; font-weight: 700; font-size: 15.5px; color: var(--ink-dark); }
  .recipient-role { position: absolute; left: 41px; top: 223px; font-family: "Montserrat", sans-serif; font-weight: 300; font-size: 10px; color: var(--ink); }
  .letter-body { position: absolute; left: 41px; top: 261px; width: 349px; font-family: "Encode Sans Condensed", sans-serif; font-weight: 300; font-size: 8.9px; line-height: 15px; color: var(--ink-dark); text-align: justify; }
  .letter-body p + p { margin-top: 15px; }
  .closing { position: absolute; left: 41px; top: 428px; font-family: "Encode Sans Condensed", sans-serif; font-weight: 300; font-size: 10px; color: var(--ink-dark); }
  .signature { position: absolute; left: 41px; top: 452px; width: 44px; height: 30px; background: linear-gradient(120deg, #efe9d6, #e3d9b8); border-radius: 4px; }
  .contact { position: absolute; color: #fff; text-align: right; font-family: "Lato", sans-serif; font-weight: 300; }
  .letterhead .contact { right: 40px; top: 533px; font-size: 8px; line-height: 9.6px; }
  .contact .gap { height: 4.5px; }
  .contact .row { display: flex; justify-content: flex-end; align-items: center; gap: 5px; line-height: 11px; }
  .contact .icon { width: 7px; height: 7px; display: block; }

  /* Business cards */
  .card { width: 182px; height: 104px; }
  .card-front { left: 635px; top: 112px; }
  .card-front .footer-band { height: 42px; }
  .card-back { left: 904px; top: 111px; background: var(--navy); }
  .card-name { position: absolute; right: 11px; top: 14px; font-family: "Montserrat", sans-serif; font-weight: 700; font-size: 8.5px; color: var(--gold); }
  .card-role { position: absolute; right: 11px; top: 25px; font-family: "Montserrat", sans-serif; font-size: 4.3px; color: var(--navy); }
  .card-front .brand-name { left: 14px; top: 48px; font-size: 7.5px; }
  .card-front .contact { right: 11px; top: 66px; font-size: 3.9px; line-height: 5px; font-weight: 400; }
  .card-front .contact .row { gap: 3px; line-height: 6.3px; }
  .card-front .contact .gap { height: 3px; }
  .card-front .contact .icon { width: 4px; height: 4px; }
  .card-back .brand-name { left: 0; width: 100%; top: 66px; text-align: center; font-size: 11px; }

  /* Envelopes */
  .envelope { left: 635px; width: 451px; height: 226px; }
  .envelope-back { top: 248px; }
  .envelope-flap { position: absolute; left: 0; top: 0; width: 100%; height: 66px; }
  .envelope-back .brand-name { left: 0; width: 100%; top: 26px; text-align: center; font-size: 9px; }
  .envelope-front { top: 494px; }
  .envelope-front .footer-band { height: 62px; }
  .envelope-front .brand-name { left: 45px; top: 95px; font-size: 16px; }
  .return-address { position: absolute; left: 308px; top: 185px; padding-left: 11px; border-left: 1px solid #fff; color: #fff; font-size: 8px; line-height: 9.4px; font-weight: 300; }
</style>
</head>
<body>

<section class="sheet letterhead">
  <div class="footer-band" role="img" aria-label="Navy footer band with gold accent"></div>
  <div class="brand-name">Beacon Law</div>
  <div class="letter-date">01 December, 2021</div>
  <div class="recipient-name">DANIEL REED</div>
  <div class="recipient-role">Cheif Executive Officer</div>
  <div class="letter-body">
    <p>Contrary to popular belief, Lorem Ipsum is not simply random text. It has roots in a piece of classical Latin literature from 45 BC, making it over 2000 years old. Arthur Linwood, a Latin professor at Kessler College in Virginia, looked up one of the more obscure Latin words, consectetur.</p>
    <p>Lorem Ipsum comes from sections 1.10.32 and 1.10.33 of "de Finibus Bonorum et Malorum" (The Extremes of Good and Evil) by Marcus Velden, written in 45 BC. This book is a treatise on the theory of ethics, very popular during the Renaissance. The first line of Lorem Ipsum.</p>
    <p>The standard chunk of Lorem Ipsum used since the 1500s is reproduced below for those interested.</p>
  </div>
  <div class="closing">Best Regards</div>
  <div class="signature" role="img" aria-label="Handwritten signature of Reed"></div>
  <div class="contact">
    <div>1234 First Line Address</div>
    <div>5678 Second Line Address</div>
    <div class="gap"></div>
    <div class="row">(777) 888-7777
      <svg class="icon" viewBox="0 0 10 10"><path d="M2,1 L4,1 L4.6,3.2 L3.4,4 C4,5.4 4.8,6.2 6,6.8 L6.8,5.6 L9,6.2 L9,8.2 C5,8.6 1.4,5 2,1 Z" fill="var(--gold)"/></svg></div>
    <div class="row">info@yourmail.com
      <svg class="icon" viewBox="0 0 10 10"><rect x="0.5" y="2" width="9" height="6.4" fill="var(--gold)"/><path d="M0.5,2 L5,5.6 L9.5,2" fill="none" stroke="var(--navy)" stroke-width="0.8"/></svg></div>
    <div class="row">www.yourwebsite.com
      <svg class="icon" viewBox="0 0 10 10"><circle cx="5" cy="5" r="4.3" fill="var(--gold)"/><path d="M0.7,5 H9.3 M5,0.7 V9.3" fill="none" stroke="var(--navy)" stroke-width="0.6"/></svg></div>
  </div>
</section>

<section class="sheet card card-front">
  <div class="footer-band" role="img" aria-label="Navy footer band with gold accent"></div>
  <div class="card-name">OWEN HALE</div>
  <div class="card-role">Founder &amp; CEO</div>
  <div class="brand-name">Beacon Law</div>
  <div class="contact">
    <div>1234 First Line Address</div>
    <div>5678 Second Line Address</div>
    <div class="gap"></div>
    <div class="row">(777) 888-7777
      <svg class="icon" viewBox="0 0 10 10"><path d="M2,1 L4,1 L4.6,3.2 L3.4,4 C4,5.4 4.8,6.2 6,6.8 L6.8,5.6 L9,6.2 L9,8.2 C5,8.6 1.4,5 2,1 Z" fill="var(--gold)"/></svg></div>
    <div class="row">info@yourmail.com
      <svg class="icon" viewBox="0 0 10 10"><rect x="0.5" y="2" width="9" height="6.4" fill="var(--gold)"/></svg></div>
    <div class="row">www.yourwebsite.com
      <svg class="icon" viewBox="0 0 10 10"><circle cx="5" cy="5" r="4.3" fill="var(--gold)"/></svg></div>
  </div>
</section>

<section class="sheet card card-back">
  <div class="brand-name">Beacon Law</div>
</section>

<section class="sheet envelope envelope-back">
  <svg class="envelope-flap" viewBox="0 0 866 126" preserveAspectRatio="none" aria-hidden="true">
    <path d="M0,0 H866 L857,76 Q850,126 800,126 H66 Q14,126 9,76 Z" fill="var(--navy)"/>
  </svg>
  <div class="brand-name">Beacon Law</div>
</section>

<section class="sheet envelope envelope-front">
  <div class="footer-band" role="img" aria-label="Navy footer band with gold accent"></div>
  <div class="brand-name">Beacon Law</div>
  <div class="return-address">
    <div>1234 First Line Address</div>
    <div>5678 Second Line Address</div>
  </div>
</section>

</body>
</html>
```